Business Card Design Project

I have attached the logo and the colour pallete for the branding for the company.

Creative designs for business cards are needed.

The Company is modern corporate.

Industry/Entity Type

Business

```html
<!DOCTYPE html>
<html lang="en">
<head>
<meta charset="utf-8">
<title>Pathwise Business Cards</title>
<link rel="stylesheet" href="https://fonts.googleapis.com/css2?family=Montserrat:wght@300;600;700&display=swap">
<style>
  :root {
    --plum-deep: #3d1540;
    --plum-bright: #6e2863;
    --plum-ink: #6b2462;
    --orange: #ee6a30;
    --grey-soft: #cfcfd1;
    --text-grey: #9a9a9a;
    --label-grey: #777777;
    --paper: #ffffff;
    --stage: #ffffff;
  }
  * { margin: 0; padding: 0; box-sizing: border-box; }
  html, body {
    width: 1200px; height: 1000px; overflow: hidden;
    background: var(--stage);
    font-family: "Montserrat", Arial, sans-serif;
  }
  .canvas { position: relative; width: 1200px; height: 1000px; }

  .card {
    position: absolute; top: 379px; width: 442px; height: 251px;
    box-shadow: 5px 5px 7px rgba(0,0,0,0.28);
  }
  .card--front {
    left: 120px;
    background: linear-gradient(90deg, var(--plum-deep) 0%, var(--plum-bright) 52%, var(--plum-deep) 100%);
    display: flex; align-items: center; justify-content: center;
  }
  .card--back {
    left: 618px; width: 440px;
    background: var(--paper);
  }

  .brand-name {
    font-weight: 600; letter-spacing: -0.5px; line-height: 1;
  }
  .card--front .brand-name {
    color: var(--paper); font-size: 58px; margin-top: 8px;
  }
  .card--back .brand-name {
    position: absolute; left: 48px; top: 167px;
    color: var(--plum-ink); font-size: 42px;
  }

  .decor-splash {
    position: absolute; left: 4px; top: 0; width: 152px; height: 110px;
  }

  .contact-divider {
    position: absolute; left: 252px; top: 165px; width: 1px; height: 47px;
    background: #c9c9c9;
  }
  .contact-list {
    position: absolute; left: 263px; top: 165px;
    list-style: none; font-size: 11.5px; font-weight: 300;
    color: var(--text-grey); line-height: 15px;
  }
  .contact-list .label { font-weight: 700; color: var(--label-grey); }
</style>
</head>
<body>
<main class="canvas">
  <section class="card card--front">
    <span class="brand-name">pathwise</span>
  </section>

  <section class="card card--back">
    <svg class="decor-splash" viewBox="0 0 152 110" role="img" aria-label="Decorative cluster of flowing droplet shapes in purple, orange and grey">
      <defs>
        <linearGradient id="splashTone" x1="0" y1="0" x2="1" y2="1">
          <stop offset="0" stop-color="#ee6a30"/>
          <stop offset="0.45" stop-color="#6e2863"/>
          <stop offset="1" stop-color="#cfcfd1"/>
        </linearGradient>
      </defs>
      <rect width="152" height="110" fill="url(#splashTone)" opacity="0.55"/>
    </svg>

    <span class="brand-name">pathwise</span>
    <div class="contact-divider"></div>
    <ul class="contact-list">
      <li><span class="label">e.</span> info@pathwise.com</li>
      <li><span class="label">t.</span> (555) 123-4567</li>
      <li><span class="label">w.</span> www.pathwise.com</li>
    </ul>
  </section>
</main>
</body>
</html>
```